Pel'k Marrowind Travel

We need a sleek, professional, inviting card to elicit global travel for the experienced and professional traveler. Royal blue, black and silver. (perhaps the wording could be silver with black shadow?-get creative) Maybe a watermark on the front and the full raised logo on the back.
We want a stylish and modern card, but professional.

```html
<!DOCTYPE html>
<html lang="en">
<head>
<meta charset="utf-8">
<title>Pel'k Marrowind Travel – Business Card</title>
<link rel="stylesheet" href="https://fonts.googleapis.com/css2?family=Montserrat:wght@500;600;700&family=Arimo:wght@400&display=swap">
<style>
  :root {
    --bg: #2a2a2b;
    --card: #1c1d1f;
    --card-back: #17181a;
    --pattern: #202123;
    --blue: #1fa3e0;
    --green: #7cc242;
    --text: #d9d9d9;
    --muted: #bfbfbf;
    --rule: #555;
  }
  * { box-sizing: border-box; margin: 0; padding: 0; }
  html, body { width: 1200px; height: 1108px; overflow: hidden; }
  body {
    background: var(--bg);
    font-family: "Arimo", Arial, sans-serif;
    position: relative;
  }
  .card {
    position: absolute;
    top: 230px;
    width: 380px;
    height: 620px;
    border-radius: 22px;
    box-shadow: 0 18px 40px rgba(0,0,0,.55);
    overflow: hidden;
  }
  .card-front { left: 170px; background: var(--card); text-align: center; }
  .card-back { left: 650px; background: var(--card-back); }

  .brand {
    margin-top: 120px;
    font-family: "Montserrat", sans-serif;
    font-weight: 700;
    color: var(--blue);
    font-size: 27px;
    line-height: 1.2;
    letter-spacing: .5px;
    text-transform: uppercase;
  }
  .brand-rule {
    width: 300px; height: 2px; margin: 16px auto 0;
    background: var(--green);
  }
  .holder-name {
    margin-top: 70px;
    font-family: "Montserrat", sans-serif;
    font-weight: 700;
    font-size: 24px;
    color: var(--blue);
    text-transform: uppercase;
  }
  .holder-title {
    margin-top: 4px;
    font-size: 16px;
    color: var(--muted);
    text-transform: uppercase;
    letter-spacing: .5px;
  }
  .icon-row {
    margin: 24px auto 0;
    display: flex; align-items: center; justify-content: center; gap: 8px;
  }
  .icon-row .line { width: 50px; height: 1px; background: var(--rule); }
  .icon {
    width: 34px; height: 34px; border-radius: 5px;
    background: var(--blue);
    display: flex; align-items: center; justify-content: center;
  }
  .contact { margin-top: 18px; list-style: none; font-size: 19px; line-height: 1.45; color: var(--text); }
  .contact .accent { color: var(--blue); }
  .divider { width: 250px; height: 1px; margin: 12px auto; background: var(--rule); }
  .address { font-size: 19px; line-height: 1.4; color: var(--text); font-style: normal; }

  .pattern-field { position: absolute; inset: 0; background: var(--pattern); }
  .back-name {
    position: absolute; left: 0; right: 0; top: 440px;
    text-align: center;
    font-family: "Montserrat", sans-serif;
    font-weight: 700;
    font-size: 24px;
    color: var(--blue);
    text-transform: uppercase;
  }
</style>
</head>
<body>
  <section class="card card-front">
    <h1 class="brand">Pel'k Marrowind<br>Travel</h1>
    <div class="brand-rule"></div>

    <h2 class="holder-name">Dorian Vale</h2>
    <p class="holder-title">Managing Director</p>

    <div class="icon-row">
      <span class="line"></span>
      <span class="icon" aria-label="Phone">
        <svg width="20" height="20" viewBox="0 0 24 24"><path fill="#1c1d1f" d="M6.6 10.8a15 15 0 0 0 6.6 6.6l2.2-2.2c.3-.3.7-.4 1-.2 1.1.4 2.3.6 3.6.6.6 0 1 .4 1 1V20c0 .6-.4 1-1 1A17 17 0 0 1 3 4c0-.6.4-1 1-1h3.5c.6 0 1 .4 1 1 0 1.3.2 2.5.6 3.6.1.3 0 .7-.2 1z"/></svg>
      </span>
      <span class="icon" aria-label="Mobile">
        <svg width="20" height="20" viewBox="0 0 24 24"><rect x="6" y="2" width="12" height="20" rx="2" fill="none" stroke="#1c1d1f" stroke-width="2"/><circle cx="12" cy="18" r="1.2" fill="#1c1d1f"/></svg>
      </span>
      <span class="icon" aria-label="Email">
        <svg width="20" height="20" viewBox="0 0 24 24"><rect x="3" y="5" width="18" height="14" fill="none" stroke="#1c1d1f" stroke-width="2"/><path d="M3 5l9 8 9-8M3 19l7-6M21 19l-7-6" fill="none" stroke="#1c1d1f" stroke-width="1.6"/></svg>
      </span>
      <span class="icon" aria-label="Website">
        <svg width="20" height="20" viewBox="0 0 24 24"><circle cx="12" cy="12" r="9" fill="none" stroke="#1c1d1f" stroke-width="2"/><path d="M3 12h18M12 3c3 3 3 15 0 18M12 3c-3 3-3 15 0 18" fill="none" stroke="#1c1d1f" stroke-width="1.5"/></svg>
      </span>
      <span class="line"></span>
    </div>

    <ul class="contact">
      <li>044-555 018 246</li>
      <li>044-555 018 246</li>
      <li>hello@marrowind.com</li>
      <li>www.<span class="accent">marrowindtravel</span>.com</li>
    </ul>
    <div class="divider"></div>
    <address class="address">421, Address line here<br>45452, Country Name</address>
  </section>

  <section class="card card-back">
    <div class="pattern-field" role="img" aria-label="Faint embossed repeating brand pattern in dark grey"></div>
    <p class="back-name">Pel'k Marrowind Travel</p>
  </section>
</body>
</html>
```